All-natural soap packaging design for new company

The box type has been selected, we just need artwork for each of our 10 products. I'd like the same look to each, the idea is just to switch out the name and ingredient label on each. The dimensions are 3.5"x3.75"x1.25". The colors in the uploaded pictures with product titles are not mandatory. I'd like to keep the font on the packaging (Rubik) as it is the same as the website.

Target Market(s)

Health & Beauty, people looking for natural or organic products

Industry/Entity Type

It Company

Colors

Designer to choose colors to be used in the design.

Requirements
Must have
• Design must be clean and relatively simple. Slightly different look for each of the 10 products. Audience is people looking for all-natural products.

```html
<!DOCTYPE html>
<html lang="en">
<head>
<meta charset="utf-8">
<title>Birchwell Soap Co. – Bar Soap Packaging Range</title>
<link href="https://fonts.googleapis.com/css2?family=Rubik:wght@400;500&display=swap" rel="stylesheet">
<style>
  :root {
    --page-bg: #e5e5e5;
    --frame: #4a4646;
    --ink: #2b2828;
    --drawer: #f1e6e8;
    --drawer-edge: #e3d3d6;
    --tab: #2e2c2c;
  }
  * { box-sizing: border-box; margin: 0; padding: 0; }
  html, body { width: 1200px; height: 1200px; overflow: hidden; }
  body {
    background: var(--page-bg);
    font-family: "Rubik", sans-serif;
    color: var(--ink);
    position: relative;
  }
  .box { position: absolute; width: 40em; height: 16.2em; }
  .box--lg { font-size: 14px; }
  .box--sm { font-size: 7px; }

  .drawer {
    position: absolute; left: 22.9em; top: 0.4em;
    width: 14em; height: 15.3em;
    background: var(--drawer);
    border: 0.15em solid var(--drawer-edge);
  }
  .drawer__seal {
    position: absolute; left: 0.5em; top: 50%;
    width: 1.9em; height: 1.9em; margin-top: -0.95em;
    border-radius: 50%; background: #f7f3f4;
  }
  .drawer__tab {
    position: absolute; right: -0.9em; top: 45%;
    width: 0.9em; height: 1.1em; background: var(--tab);
  }

  .sleeve {
    position: absolute; left: 0; top: 0;
    width: 23.7em; height: 16.1em;
    border: 0.22em solid var(--frame);
    background: radial-gradient(circle at 30% 30%, #ffffff, var(--tint));
    overflow: hidden;
  }
  .sleeve__brand {
    position: absolute; left: 0; right: 0; top: 1.2em;
    display: flex; flex-direction: column; align-items: center; gap: 0.5em;
  }
  .sleeve__mark { width: 2.6em; height: 2.6em; background: var(--frame); }
  .sleeve__name {
    font-size: 0.6em; font-weight: 500; letter-spacing: 0.05em;
    color: var(--frame); text-transform: uppercase;
  }
  .sleeve__band {
    position: absolute; left: 0; right: 0; top: 50.5%; height: 21%;
    background: var(--accent);
    border-top: 0.15em solid var(--frame);
    border-bottom: 0.15em solid var(--frame);
    display: flex; align-items: center; justify-content: center;
  }
  .sleeve__title {
    font-size: 1.05em; font-weight: 400; letter-spacing: 0.2em;
    text-transform: uppercase; white-space: nowrap;
  }
  .box--sm .sleeve__title { font-size: 1.15em; letter-spacing: 0.18em; }
  .sleeve__weight {
    position: absolute; left: 0; right: 0; top: 80%;
    text-align: center; font-size: 0.95em;
  }
</style>
</head>
<body>

<!-- Peppermint + Tamanu -->
<div class="box box--lg" style="left:32px;top:184px;--accent:#f8c0c0;--tint:#ecdcdc">
  <div class="drawer" role="img" aria-label="Drawer wrap with diagonal leaf pattern"><span class="drawer__seal"></span><span class="drawer__tab"></span></div>
  <div class="sleeve" role="img" aria-label="Soft soap lather bubbles background">
    <div class="sleeve__brand"><span class="sleeve__mark"></span><span class="sleeve__name">Birchwell Soap Co.</span></div>
    <div class="sleeve__band"><span class="sleeve__title">Peppermint + Tamanu</span></div>
    <div class="sleeve__weight">100g</div>
  </div>
</div>

<div class="box box--sm" style="left:617px;top:92px;--accent:#f0c088;--tint:#e9e4da">
  <div class="drawer" role="img" aria-label="Drawer wrap with diagonal leaf pattern"><span class="drawer__seal"></span><span class="drawer__tab"></span></div>
  <div class="sleeve" role="img" aria-label="Soft soap lather bubbles background">
    <div class="sleeve__brand"><span class="sleeve__mark"></span><span class="sleeve__name">Birchwell Soap Co.</span></div>
    <div class="sleeve__band"><span class="sleeve__title">Carrot + Ginger</span></div>
    <div class="sleeve__weight">100g</div>
  </div>
</div>

<div class="box box--sm" style="left:917px;top:92px;--accent:#f8e39a;--tint:#e8e6da">
  <div class="drawer" role="img" aria-label="Drawer wrap with diagonal leaf pattern"><span class="drawer__seal"></span><span class="drawer__tab"></span></div>
  <div class="sleeve" role="img" aria-label="Soft soap lather bubbles background">
    <div class="sleeve__brand"><span class="sleeve__mark"></span><span class="sleeve__name">Birchwell Soap Co.</span></div>
    <div class="sleeve__band"><span class="sleeve__title">Calendula + Chamomile</span></div>
    <div class="sleeve__weight">100g</div>
  </div>
</div>

<div class="box box--sm" style="left:617px;top:392px;--accent:#fbe3a0;--tint:#e8e6dc">
  <div class="drawer" role="img" aria-label="Drawer wrap with diagonal leaf pattern"><span class="drawer__seal"></span><span class="drawer__tab"></span></div>
  <div class="sleeve" role="img" aria-label="Soft soap lather bubbles background">
    <div class="sleeve__brand"><span class="sleeve__mark"></span><span class="sleeve__name">Birchwell Soap Co.</span></div>
    <div class="sleeve__band"><span class="sleeve__title">Papaya + Rosehip</span></div>
    <div class="sleeve__weight">100g</div>
  </div>
</div>

<div class="box box--sm" style="left:917px;top:392px;--accent:#c2f0a8;--tint:#e1e6de">
  <div class="drawer" role="img" aria-label="Drawer wrap with diagonal leaf pattern"><span class="drawer__seal"></span><span class="drawer__tab"></span></div>
  <div class="sleeve" role="img" aria-label="Soft soap lather bubbles background">
    <div class="sleeve__brand"><span class="sleeve__mark"></span><span class="sleeve__name">Birchwell Soap Co.</span></div>
    <div class="sleeve__band"><span class="sleeve__title">Jojoba + Lemon Grass</span></div>
    <div class="sleeve__weight">100g</div>
  </div>
</div>

<div class="box box--sm" style="left:18px;top:692px;--accent:#bdbdbd;--tint:#dcdcdc">
  <div class="drawer" role="img" aria-label="Drawer wrap with diagonal leaf pattern"><span class="drawer__seal"></span><span class="drawer__tab"></span></div>
  <div class="sleeve" role="img" aria-label="Soft soap lather bubbles background">
    <div class="sleeve__brand"><span class="sleeve__mark"></span><span class="sleeve__name">Birchwell Soap Co.</span></div>
    <div class="sleeve__band"><span class="sleeve__title" style="font-size:0.95em;letter-spacing:0.12em">Activated Charcoal + Bavarian Beer</span></div>
    <div class="sleeve__weight">100g</div>
  </div>
</div>

<div class="box box--sm" style="left:318px;top:692px;--accent:#7f9bd2;--tint:#dee0ea">
  <div class="drawer" role="img" aria-label="Drawer wrap with diagonal leaf pattern"><span class="drawer__seal"></span><span class="drawer__tab"></span></div>
  <div class="sleeve" role="img" aria-label="Soft soap lather bubbles background">
    <div class="sleeve__brand"><span class="sleeve__mark"></span><span class="sleeve__name">Birchwell Soap Co.</span></div>
    <div class="sleeve__band"><span class="sleeve__title">Hemp + Borage</span></div>
    <div class="sleeve__weight">100g</div>
  </div>
</div>

<div class="box box--sm" style="left:18px;top:992px;--accent:#f0c6ec;--tint:#e5dfe6">
  <div class="drawer" role="img" aria-label="Drawer wrap with diagonal leaf pattern"><span class="drawer__seal"></span><span class="drawer__tab"></span></div>
  <div class="sleeve" role="img" aria-label="Soft soap lather bubbles background">
    <div class="sleeve__brand"><span class="sleeve__mark"></span><span class="sleeve__name">Birchwell Soap Co.</span></div>
    <div class="sleeve__band"><span class="sleeve__title">Lavender + Witch Hazel</span></div>
    <div class="sleeve__weight">100g</div>
  </div>
</div>

<div class="box box--sm" style="left:318px;top:992px;--accent:#8fd0f0;--tint:#dde6ea">
  <div class="drawer" role="img" aria-label="Drawer wrap with diagonal leaf pattern"><span class="drawer__seal"></span><span class="drawer__tab"></span></div>
  <div class="sleeve" role="img" aria-label="Soft soap lather bubbles background">
    <div class="sleeve__brand"><span class="sleeve__mark"></span><span class="sleeve__name">Birchwell Soap Co.</span></div>
    <div class="sleeve__band"><span class="sleeve__title">Seabuckthorn + Bilberry</span></div>
    <div class="sleeve__weight">100g</div>
  </div>
</div>

<!-- Aloe Vera + Eucalyptus -->
<div class="box box--lg" style="left:633px;top:783px;--accent:#c8fadc;--tint:#dfe7e2">
  <div class="drawer" role="img" aria-label="Drawer wrap with diagonal leaf pattern"><span class="drawer__seal"></span><span class="drawer__tab"></span></div>
  <div class="sleeve" role="img" aria-label="Soft soap lather bubbles background">
    <div class="sleeve__brand"><span class="sleeve__mark"></span><span class="sleeve__name">Birchwell Soap Co.</span></div>
    <div class="sleeve__band"><span class="sleeve__title">Aloe Vera + Eucalyptus</span></div>
    <div class="sleeve__weight">100g</div>
  </div>
</div>

</body>
</html>
```